Interim / Part-time CFO Flyer

We need a flyer design for our existing business that is capable of being emailed and printed.

We provide business advisory services lanternridge.com.au.Please consult our website to get a feel for the style of flyer.

We need to attract a potential customer quickly. The attached wording may contain too much so please feel free to edit.

PLEASE NOTE THAT THE ATTACHED .ai and .eps FILES SHOULD BE FOR Lantern Ridge "Business Advisory" (not "Corporate Advisory") I can't open it to check.

***note i have just uploaded replacement copy for flyer*****

Target Market(s)

Businesses

Font styles to use
Other font styles liked:
• Open Sans

Colors
3276b5
cedeeb
f2f0f5

Requirements
Must have
• Catchy title, remembering that this is directed at businesses

```html
<!DOCTYPE html>
<html lang="en">
<head>
<meta charset="utf-8">
<title>Lantern Ridge – Interim &amp; Part Time CFO</title>
<link href="https://fonts.googleapis.com/css2?family=Arimo:wght@400;700&family=Questrial&display=swap" rel="stylesheet">
<style>
  :root{
    --brand-blue:#3276b5;
    --brand-navy:#1f3f8f;
    --hero-blue:#4d8fcc;
    --hero-deep:#3a78b8;
    --pale-blue:#cedeeb;
    --paper:#f7f7f9;
    --side-grey:#e3e3e6;
    --ink:#2b2b2b;
    --footer-top:#5b9ad6;
    --footer-bottom:#2e6aaa;
  }
  html,body{margin:0;padding:0;overflow:hidden;}
  body{width:912px;height:1200px;background:var(--paper);font-family:'Arimo',Arial,sans-serif;color:var(--ink);position:relative;}
  .flyer{position:relative;width:912px;height:1200px;overflow:hidden;}

  .masthead{position:absolute;left:0;top:0;width:912px;height:127px;}
  .brand{position:absolute;left:24px;top:34px;display:flex;align-items:center;gap:14px;}
  .brand-mark{width:64px;height:64px;border-radius:50%;background:var(--brand-navy);}
  .brand-name{font-size:34px;font-weight:700;color:var(--brand-navy);line-height:1;letter-spacing:-0.3px;}
  .brand-tagline{font-size:27px;color:var(--brand-blue);line-height:1.15;margin-top:3px;}

  .hero{position:absolute;left:0;top:127px;width:912px;height:258px;background:linear-gradient(180deg,var(--hero-blue),var(--hero-deep));}
  .hero-title{position:absolute;left:52px;top:70px;margin:0;font-family:'Questrial','Century Gothic',sans-serif;font-weight:400;font-size:58px;line-height:74px;color:#fff;}
  .hero-photo{position:absolute;right:0;top:0;width:438px;height:258px;background:linear-gradient(160deg,#f4f5f7,#d6d9de 70%,#b9bec6);}

  .sidebar{position:absolute;left:0;top:402px;width:346px;height:708px;background:var(--side-grey);padding:12px 6px 0 19px;box-sizing:border-box;}
  .main{position:absolute;left:358px;top:402px;width:542px;padding-top:10px;}

  .section-title{font-size:17.5px;line-height:20px;font-weight:400;color:var(--brand-navy);margin:0 0 10px;padding-bottom:5px;border-bottom:1px solid #b7bcc6;}
  .main .section-title{border-bottom:1px solid #c9ccd3;margin-bottom:13px;}
  p{margin:0 0 17px;font-size:13.4px;line-height:20px;}
  .sidebar p{line-height:20.5px;}
  .sidebar .section-title.second{margin-top:-4px;margin-bottom:10px;}

  .point{display:flex;align-items:center;gap:10px;font-size:17px;line-height:20px;font-weight:700;color:#111;margin:-6px 0 5px 10px;}
  .point::before{content:"";width:8px;height:8px;border-radius:50%;background:var(--brand-navy);}

  .footer{position:absolute;left:0;top:1110px;width:912px;height:90px;background:linear-gradient(180deg,var(--footer-top),var(--footer-bottom));color:#fff;text-align:center;font-size:13.4px;line-height:21px;padding-top:8px;box-sizing:border-box;}
</style>
</head>
<body>
<div class="flyer">
  <header class="masthead">
    <div class="brand">
      <div class="brand-mark"></div>
      <div>
        <div class="brand-name">Lantern Ridge</div>
        <div class="brand-tagline">Business Advisory</div>
      </div>
    </div>
  </header>

  <section class="hero">
    <h1 class="hero-title">Our People<br>Your Potential</h1>
    <div class="hero-photo" role="img" aria-label="Photograph of a confident team of business professionals in suits, arms folded"></div>
  </section>

  <aside class="sidebar">
    <h2 class="section-title">Interim CFO / Financial Controller</h2>
    <p>Experiencing rapid growth or change? Is year-end getting on top of you? Maybe your CFO or Financial Controller just gave notice. If you are unexpectedly losing a key member of your finance or accounting team and are looking for a solution like an interim employee, Lantern Ridge is ready to help.</p>
    <p>Getting on top of a backlog of work takes some doing, sometimes it can be hard to know where to start. Often faced with deadlines, work gets done in less than ideal ways on the understanding that it will be sorted out properly next time.</p>
    <p>A Lantern Ridge expert can serve as an interim CFO, financial controller, treasurer, and accountant. We have the experience in-house to provide your organisation with an accounting professional that will quickly learn your company’s operations and keep your business running. We can fill temporary staff vacancies quickly and easily with experienced senior level accounting professionals who know and understand your industry.</p>
    <h2 class="section-title second">No Time Defined Contracts</h2>
    <p>We work with a handshake on an affordable as-needed basis. No time defined contract is required to engage our partners.</p>
    <p>If you are already paying quite a lot of money and not getting all the information you would like to run your business - the problem is most likely process design, not the people.</p>
  </aside>

  <main class="main">
    <h2 class="section-title">Part Time CFO / Financial Controller</h2>
    <p>Ideally companies would prefer to have an available CFOor Financial Controller resource for banking relationships, auditor interfaces, internal control, accounting procedures, management, policies and overall strategy development.</p>
    <p>You need a CFO available, but not necessarily full-time. Why incur the on-costs when you can have a CFO accessible at all times?</p>

    <div class="point">Financial &amp; Goal Clarity</div>
    <p>We work with the business owner to create financial and goal clarity. We try to understand the overall goals that our clients want to achieve. We then work with the business owner to create financial clarity in order to achieve those goals.</p>

    <div class="point">Trusted, Long-Term Business Advisor</div>
    <p>Lantern Ridge is a trusted business advisor. Our goal is to have a long-term business relationship with our clients, similar to those that our clients have with their solicitor and tax accountant.</p>
    <p>A Lantern Ridge CFO stays long-term with the company to help the company grow and to help valuable information remain with the company.</p>

    <div class="point">Seasoned Partners</div>
    <p>Services are provided on an objective basis by seasoned partners who average 13 years of CFO experience. It is highly unlikely that a company will ask a question or present a problem that our experienced partners can’t resolve.</p>
    <p>Lantern Ridge professionals work part-time within your organisation to solve problems and address your immediate finance and accounting needs. Lantern Ridge can provide part-time CFOs, controllers, and senior accountants.</p>
    <p>Lantern Ridge has established a robust set of operating procedures on how to setup a company’s books and records to “automate” the process of closing a company’s financial records on a monthly basis, and manage the accounting and finance department. Our professionals provide your business with flexibility, and can take on additional projects as your business expands.</p>
  </main>

  <footer class="footer">
    Halvard Pty Limited | ABN 41 203 558 917<br>
    Phone: 02 9000 4127 | Fax: 02 9000 4128 | Level 2, 145 Marlow Street Redfield NSW 2090<br>
    Email: admin@lanternridge.com.au | Web: www.lanternridge.com.au
  </footer>
</div>
</body>
</html>
```